NOT HAPPY FLYER

The brochure is for a Real Estate Agent, as a prospecting tool for upmarket, expensive homes.

BRIEF:
On the first side will be:
NOT HAPPY? (in a funky font)
(Have a picture of maybe an unhappy dog, or something that displays unhappiness on the front)

The second side:
-With your current service and advice?
Need a result NOW?
-Want a second opinion?

If you have been on the market for over 45 days with no results, it’s time to question why.

Nora Pemberley (photo of Nora)
Your Modern, Local Real Estate Agent.

It is no secret that the greater the exposure a property has to the market, the greater the number of buyers who are aware of the listing. Every property is unique and Nora ensures that each property has its own tailored marketing plan, so your property stands out from the crowd.

Whether you’re considering buying locally or internationally, Nora will work with you to towards understanding those special qualities and those requirements you seek.
If you want to combine these components into an advantageous world class real estate transaction, call Nora Pemberley.

W: (WEBSITE HERE)
M: (MOBILE HERE)
E: (EMAIL HERE)

Target Market(s)

The target market are people who own upmarket, expensive properties.

Industry/Entity Type

Real Estate

Font styles to use
Decorative

Requirements
Must have
• Must be fun, yet professional. Needs to stand out. It will be printed in matt gloss laminate, so it will look very exclusive.

Second side with my photo and a small Ho/vel logo
Nice to have
• Have some funky fonts.

```html
<!DOCTYPE html>
<html lang="en">
<head>
<meta charset="utf-8">
<title>Not Happy? – Nora Pemberley Flyer</title>
<link rel="stylesheet" href="https://fonts.googleapis.com/css2?family=Luckiest+Guy&family=Sniglet:wght@800&family=Cabin:wght@400&family=Arimo:wght@400;700&display=swap">
<style>
  :root {
    --page: #ffffff;
    --gold-light: #f6d27a;
    --gold: #d99a1e;
    --gold-deep: #8a5208;
    --gold-dark: #5a3104;
    --ink: #2a1a08;
    --white: #ffffff;
    --brand-box: #1a1a1a;
    --shadow: rgba(0,0,0,0.35);
  }
  * { margin: 0; padding: 0; box-sizing: border-box; }
  html, body { width: 829px; height: 1200px; overflow: hidden; background: var(--page); }
  .canvas { position: relative; width: 829px; height: 1200px; }

  .card {
    position: absolute;
    overflow: hidden;
    box-shadow: 3px 3px 4px var(--shadow);
  }
  .card--front { left: 32px; top: 44px; width: 768px; height: 526px;
    background: radial-gradient(ellipse 60% 55% at 62% 38%, var(--gold-light) 0%, var(--gold) 45%, var(--gold-deep) 85%, var(--gold-dark) 100%); }
  .card--back  { left: 38px; top: 628px; width: 753px; height: 528px;
    background: radial-gradient(ellipse 70% 60% at 45% 45%, var(--gold-light) 0%, var(--gold) 50%, var(--gold-deep) 90%, var(--gold-dark) 100%); }

  /* Front */
  .hero-photo {
    position: absolute; left: 200px; top: 250px; width: 568px; height: 276px;
    background: radial-gradient(ellipse 55% 70% at 55% 70%, #6e3608 0%, #8a4610 40%, rgba(160,90,20,0.6) 70%, rgba(200,130,40,0) 100%);
  }
  .headline { position: absolute; font-family: "Luckiest Guy", "Arial Black", sans-serif; color: var(--white);
    text-shadow: 4px 4px 0 var(--ink); line-height: 1; white-space: nowrap; }
  .headline--not { left: 42px; top: 76px; font-size: 190px; letter-spacing: 2px; }
  .headline--happy { left: 56px; top: 244px; font-size: 86px; letter-spacing: 3px; }

  /* Back */
  .intro { position: absolute; left: 24px; top: 12px; font-family: "Cabin", sans-serif;
    font-size: 21px; line-height: 27px; color: var(--ink); }
  .hook { position: absolute; left: 24px; top: 66px; width: 700px; font-family: "Sniglet", sans-serif; font-weight: 800;
    font-size: 19px; line-height: 27px; color: var(--ink); white-space: nowrap; }
  .pitch { position: absolute; left: 80px; top: 165px; width: 440px; text-align: right;
    font-family: "Arimo", sans-serif; font-size: 17px; line-height: 22px; color: var(--ink); }
  .pitch__cta { display: block; margin-top: 2px; font-weight: 700; font-size: 25px; line-height: 30px; }

  .agent-photo {
    position: absolute; left: 557px; top: 151px; width: 158px; height: 206px;
    background: var(--white); padding: 8px; box-shadow: 2px 4px 8px var(--shadow);
  }
  .agent-photo__fill { width: 100%; height: 100%;
    background: linear-gradient(160deg, #4f6a3e 0%, #7a5a3a 45%, #c99a7c 70%, #2a2320 100%); }

  .brand { position: absolute; left: 34px; top: 385px; width: 96px; height: 133px;
    background: var(--brand-box); display: flex; align-items: center; justify-content: center; text-align: center;
    font-family: "Arimo", sans-serif; font-weight: 400; font-size: 15px; line-height: 19px; color: var(--white); }

  .contact { position: absolute; left: 156px; top: 404px; list-style: none;
    font-family: "Arimo", sans-serif; font-size: 17px; line-height: 28px; color: var(--ink); }
</style>
</head>
<body>
<main class="canvas">
  <section class="card card--front" aria-label="Flyer front">
    <div class="hero-photo" role="img" aria-label="Photo of a sad-looking bulldog gazing upward"></div>
    <h1 class="headline headline--not">NOT</h1>
    <p class="headline headline--happy">HAPPY?</p>
  </section>

  <section class="card card--back" aria-label="Flyer back">
    <p class="intro">With your current service and advice?<br>Need a result NOW?&nbsp; Want a second opinion?</p>
    <p class="hook">If you have been on the market for<br>over 45 days with no results, it’s time to question why.</p>
    <p class="pitch">Whether you’re considering buying locally or internationally, Nora will work with you to towards understanding those special qualities and those requirements you seek.<br>If you want to combine these components into an advantageous world class real estate transaction,
      <span class="pitch__cta">call Nora Pemberley.</span></p>
    <div class="agent-photo"><div class="agent-photo__fill" role="img" aria-label="Portrait photo of agent Nora Pemberley"></div></div>
    <div class="brand">Hovel<br>Realty</div>
    <ul class="contact">
      <li>www.hovelrealty.com</li>
      <li>Call @</li>
      <li>Write st nora@hovelrealty.com</li>
    </ul>
  </section>
</main>
</body>
</html>
```